Harrowby Lending Hard Money Lender

We are looking for this flyer to be redesigned. We would like it to be even more simple than the attached design. No photos, no exclamation points, a 3-4 color palate maximum. We would do not want any graphics around the "Harrowby Lending" logo.

```html
<!DOCTYPE html>
<html lang="en">
<head>
<meta charset="utf-8">
<title>Harrowby Lending – Hard Money Loans</title>
<link rel="stylesheet" href="https://fonts.googleapis.com/css2?family=Marcellus&family=Montserrat:ital,wght@0,400;0,800;1,800&display=swap">
<style>
  :root {
    --sky: #6199bb;
    --navy: #23214f;
    --ink: #000000;
    --white: #ffffff;
    --corner: #a9c6d7;
  }
  html, body { margin: 0; padding: 0; overflow: hidden; }
  .flyer {
    position: relative;
    width: 928px;
    height: 1200px;
    background: var(--sky);
    overflow: hidden;
    font-family: "Montserrat", sans-serif;
    color: var(--navy);
  }
  .corner { position: absolute; inset: 0; width: 928px; height: 1200px; }
  .flyer > div { position: absolute; line-height: 1; white-space: nowrap; }
  .brand-name {
    left: 0; right: 0; top: 116px; text-align: center;
    font-family: "Marcellus", serif; font-size: 92px; color: var(--ink);
  }
  .brand-sub {
    left: 0; right: 0; top: 224px; text-align: center;
    font-family: "Marcellus", serif; font-size: 32px; letter-spacing: 2px; color: var(--ink);
  }
  .headline { left: 65px; top: 379px; font-size: 62px; font-weight: 800; letter-spacing: 1px; }
  .rates { right: 79px; top: 446px; font-size: 21px; color: var(--white); letter-spacing: 0.5px; }
  .feature { left: 63px; font-size: 28px; letter-spacing: 0.5px; }
  .feature small { font-size: 18px; }
  .feature-1 { top: 578px; }
  .feature-2 { top: 637px; }
  .feature-3 { top: 694px; }
  .contact-title { left: 63px; top: 883px; font-size: 44px; font-weight: 800; letter-spacing: 1px; }
  .contact-line { left: 65px; font-size: 21px; letter-spacing: 0.5px; }
  .email { top: 947px; }
  .website { top: 990px; }
  .address { left: 65px; top: 1036px; font-size: 14px; }
  .phone { right: 64px; top: 1078px; font-size: 74px; font-weight: 800; font-style: italic; }
</style>
</head>
<body>
<main class="flyer">
  <svg class="corner" viewBox="0 0 928 1200" aria-hidden="true">
    <polygon points="0,0 81,0 0,96" fill="var(--corner)"/>
    <polygon points="928,1104 928,1200 847,1200" fill="var(--corner)"/>
  </svg>

  <div class="brand-name">HARROWBY</div>
  <div class="brand-sub">LENDING</div>

  <div class="headline">HARD MONEY LOANS</div>
  <div class="rates">Rates From 8%</div>

  <div class="feature feature-1">Same-Day Approval</div>
  <div class="feature feature-2">No Processing, Appraisal, or Extra Fees</div>
  <div class="feature feature-3">100% Financing<small>(w/ Additional Collateral)</small></div>

  <div class="contact-title">CONTACT US:</div>
  <div class="contact-line email">hello@harrowbylending.com</div>
  <div class="contact-line website">http://harrowbylending.com</div>
  <div class="address">1480 Aspen Ridge Ave., Suite 100&nbsp;&nbsp;&nbsp;Denver, CO 80219</div>

  <div class="phone">303.555.0148</div>
</main>
</body>
</html>
```